New Dental Office Needs an Attractive and user friendly Website Designed

I need a website for a new dental office. The Name is Maplecrest Dentistry. I would like a Modern design with a user friendly interface and usability.
I would like a landing page, a page that lists the services we offer: Cosmetic Dentistry, Implants, Dental Hygiene, Emergency Services, Restorations, Dentures
Target Market(s)
Mid to upper class
Industry/Entity Type
Dentistry
Coding
Coded - Design and coding required
Number of Pages Required
1 page
Requirements
Must have
- Landing page that has a scheduling option, Procedures, operating hours, and contact us info
Nice to have
- Appealing design, Soft comforting colors. Easy to navigate page, Modern and professional.

```html
<!DOCTYPE html>
<html lang="en">
<head>
<meta charset="utf-8">
<title>Maplecrest Dentistry</title>
<link href="https://fonts.googleapis.com/css2?family=Libre+Baskerville:wght@400;700&family=Roboto+Condensed:wght@300;400&family=Raleway:wght@500;600;700&family=Montserrat:ital,wght@0,400;0,500;1,400&display=swap" rel="stylesheet">
<style>
:root{
  --teal:#36b5c9;
  --teal-dark:#2aa3b7;
  --ink:#1d1d1f;
  --grey:#8a8a8a;
  --panel:#f3f5f6;
  --white:#ffffff;
}
*{margin:0;padding:0;box-sizing:border-box}
html,body{width:1200px;height:4315px;overflow:hidden;background:var(--white)}
body{position:relative;font-family:'Roboto Condensed',sans-serif;color:var(--ink)}
.abs{position:absolute}
.serif{font-family:'Libre Baskerville',serif;font-weight:700;color:var(--ink);text-transform:uppercase}
.brand{font-family:'Libre Baskerville',serif;font-weight:400;color:var(--teal);font-size:24px;line-height:1.1}
.nav a{position:absolute;top:38px;font-family:'Roboto Condensed',sans-serif;font-size:18px;color:#333;text-decoration:none}
.pill{background:var(--teal);color:var(--white);border-radius:40px;font-family:'Raleway',sans-serif;font-weight:700;text-align:center;text-transform:uppercase}
.lead{font-family:'Roboto Condensed',sans-serif;font-size:18px;line-height:26px;color:var(--grey);font-weight:300}
.stat-num{font-family:'Libre Baskerville',serif;font-size:44px;color:var(--white)}
.stat-lbl{font-family:'Montserrat',sans-serif;font-size:13px;color:var(--white);line-height:15px}
.photo{border-radius:22px}
.service{position:absolute;width:330px;text-align:center}
.service h3{font-family:'Raleway',sans-serif;font-weight:700;font-size:21px;margin-top:14px;text-transform:uppercase}
.service p{font-family:'Roboto Condensed',sans-serif;font-size:18px;line-height:26px;color:var(--grey);font-weight:300;margin-top:12px}
.step{position:absolute;width:240px;text-align:center}
.step h4{font-family:'Raleway',sans-serif;font-weight:700;font-size:18px}
.step p{font-family:'Roboto Condensed',sans-serif;font-size:11px;line-height:16px;color:var(--grey);margin-top:10px;font-weight:300}
.field{position:absolute;background:var(--white);font-family:'Montserrat',sans-serif;font-size:13px;color:#555;padding:0 24px;display:flex;align-items:center}
.foot-h{font-family:'Libre Baskerville',serif;font-size:15px;color:var(--white);text-transform:uppercase}
.foot-link{font-family:'Montserrat',sans-serif;font-size:13px;color:var(--white);text-transform:uppercase}
.foot-txt{font-family:'Montserrat',sans-serif;font-size:13px;color:var(--white);line-height:20px;white-space:nowrap}
</style>
</head>
<body>

<!-- Hero photo -->
<svg class="abs" style="left:600px;top:0" width="600" height="580" viewBox="600 0 600 580">
  <defs>
    <linearGradient id="heroGrad" x1="0" y1="0" x2="1" y2="1">
      <stop offset="0" stop-color="#dfe3e4"/><stop offset="0.6" stop-color="#d9b59a"/><stop offset="1" stop-color="#86c9c0"/>
    </linearGradient>
  </defs>
  <path d="M620,0 L1200,0 L1200,566 L1130,566 C860,560 640,320 620,0 Z" fill="#36b5c9"/>
  <path d="M634,0 L1200,0 L1200,556 L1130,556 C870,548 652,316 634,0 Z" fill="url(#heroGrad)" role="img" aria-label="Photo of a smiling woman with her hands on her cheeks"/>
</svg>

<!-- Header -->
<div class="abs brand" style="left:93px;top:38px;width:240px">Maplecrest Dentistry</div>
<nav class="nav">
  <a style="left:442px">HOME</a>
  <a style="left:535px">ABOUT</a>
  <a style="left:643px">SERVICES</a>
  <a style="left:769px">DOCTORS</a>
  <a style="left:894px">CONTACT</a>
</nav>
<div class="abs pill" style="left:1026px;top:35px;width:141px;height:27px;font-size:13px;line-height:27px">Get Appointment</div>

<!-- Hero text -->
<div class="abs" style="left:90px;top:184px;font-family:'Raleway',sans-serif;font-weight:500;font-size:24px;color:var(--teal)">WELCOME TO</div>
<h1 class="abs serif" style="left:84px;top:220px;font-size:56px;line-height:64px">Maplecrest<br>Dentistry</h1>
<p class="abs lead" style="left:87px;top:363px;width:520px">Lorem ipsum dolor sit amet, consectetuer adipiscing elit, sed diam<br>nonummy nibh euismod tincidunt ut laoreet dolore magna aliquam</p>
<div class="abs pill" style="left:89px;top:439px;width:233px;height:47px;line-height:47px;font-size:18px;font-weight:600">Get Appointment</div>

<!-- Stats -->
<div class="abs" style="left:99px;top:566px;width:769px;height:130px;border-radius:65px;background:var(--teal)"></div>
<svg class="abs" style="left:158px;top:596px" width="76" height="70" viewBox="0 0 76 70" fill="none" stroke="#fff" stroke-width="3">
  <path d="M38,38 C20,24 18,8 30,8 C35,8 38,14 38,14 C38,14 41,8 46,8 C58,8 56,24 38,38 Z"/>
  <path d="M4,44 L18,44 L18,66 L4,66 Z M18,48 C30,44 36,48 44,50 L54,52 C58,54 56,60 50,58 L38,56 M18,62 C34,66 48,66 70,50 C74,46 70,42 64,46 L54,52"/>
</svg>
<div class="abs stat-num" style="left:248px;top:588px">95K</div>
<div class="abs stat-lbl" style="left:256px;top:638px">Happy<br>Customers</div>
<svg class="abs" style="left:388px;top:596px" width="72" height="74" viewBox="0 0 72 74" fill="none" stroke="#fff" stroke-width="3">
  <rect x="6" y="4" width="60" height="26" rx="3"/>
  <path d="M18,12 l3,6 l-6,0 z M36,12 l3,6 l-6,0 z M54,12 l3,6 l-6,0 z"/>
  <path d="M4,44 L16,44 L16,70 L4,70 Z M16,46 L26,34 C30,30 34,34 32,40 L30,46 L46,46 C52,46 52,54 46,54 C52,54 52,62 46,62 C50,62 50,70 44,70 L16,70"/>
</svg>
<div class="abs stat-num" style="left:474px;top:590px">100%</div>
<div class="abs stat-lbl" style="left:478px;top:640px">Customer<br>Satisfaction</div>
<svg class="abs" style="left:632px;top:594px" width="76" height="74" viewBox="0 0 76 74" fill="none" stroke="#fff" stroke-width="3">
  <circle cx="46" cy="26" r="20"/><circle cx="46" cy="26" r="12"/>
  <path d="M40,26 l4,4 l8,-8"/>
  <path d="M4,46 L16,46 L16,70 L4,70 Z M16,50 C28,46 34,50 42,52 L52,54 C56,56 54,62 48,60 L36,58 M16,66 C32,70 46,70 70,52"/>
</svg>
<div class="abs stat-num" style="left:728px;top:588px">15+</div>
<div class="abs stat-lbl" style="left:728px;top:636px">Years of<br>Experience</div>

<!-- About -->
<div class="abs photo" role="img" aria-label="Photo of a patient having a dental check with a mirror" style="left:87px;top:897px;width:211px;height:155px;background:linear-gradient(135deg,#d8a58a,#4a8fd0)"></div>
<div class="abs photo" role="img" aria-label="Photo of a dentist talking with a patient in the chair" style="left:333px;top:841px;width:210px;height:210px;background:linear-gradient(135deg,#c9d3d8,#8fb0c0)"></div>
<div class="abs photo" role="img" aria-label="Photo of two dentists treating a patient" style="left:122px;top:1083px;width:211px;height:211px;background:linear-gradient(135deg,#b8c6d0,#e4cfc4)"></div>
<div class="abs photo" role="img" aria-label="Photo of a dentist wearing a mask holding instruments" style="left:377px;top:1069px;width:211px;height:156px;background:linear-gradient(135deg,#c8a68f,#dfe8ef)"></div>
<h2 class="abs serif" style="left:648px;top:900px;font-size:40px">About Us</h2>
<p class="abs lead" style="left:647px;top:968px;width:500px;white-space:nowrap">Lorem ipsum dolor sit amet, consectetuer adipiscing elit, sed diam<br>nonummy nibh euismod tincidunt ut laoreet dolore magna aliquam<br>erat volutpat. Ut wisi enim ad minim veniam, quis nostrud exerci tation<br>ullamcorper suscipit lobortis nisl ut aliquip ex ea commodo consequat.<br>Duis autem vel eum iriure dolor in hendrerit in vulputate velit esse mo-<br>lestie consequat, vel illum dolore eu feugiat nulla facilisis at vero eros et<br>accumsan et iusto odio dignissim qui blandit praesent luptatum zzril</p>
<div class="abs pill" style="left:647px;top:1207px;width:161px;height:37px;line-height:37px;font-size:15px;font-weight:600">Read More</div>

<!-- Services -->
<svg width="0" height="0" style="position:absolute">
  <symbol id="tooth" viewBox="-30 -30 60 60">
    <path d="M-16,-20 C-26,-20 -26,-4 -20,6 C-16,14 -16,24 -12,24 C-8,24 -8,12 0,12 C8,12 8,24 12,24 C16,24 16,14 20,6 C26,-4 26,-20 16,-20 C8,-20 6,-16 0,-16 C-6,-16 -8,-20 -16,-20 Z" fill="none" stroke="#36b5c9" stroke-width="2.2"/>
  </symbol>
</svg>
<section class="abs" style="left:0;top:1411px;width:1200px;height:910px;background:var(--panel)">
  <h2 class="abs serif" style="left:0;width:1200px;text-align:center;top:98px;font-size:40px">What We Do</h2>
  <div class="abs" style="left:446px;top:218px;width:332px;height:278px;background:var(--white);box-shadow:0 6px 24px rgba(0,0,0,.08)"></div>

  <div class="service" style="left:88px;top:230px">
    <svg width="70" height="70" viewBox="0 0 70 70"><use href="#tooth" x="0" y="0" width="60" height="70"/><circle cx="52" cy="32" r="11" fill="none" stroke="#36b5c9" stroke-width="2.2"/><path d="M52,26 v12 M46,32 h12" stroke="#36b5c9" stroke-width="2.2"/></svg>
    <h3>Cosmetic Dentistry</h3>
    <p>Lorem ipsum dolor sit amet,<br>consectetur adipiscing elit, sed do<br>eiusmod tempor incididunt</p>
  </div>
  <div class="service" style="left:447px;top:236px">
    <svg width="60" height="80" viewBox="0 0 60 80" fill="none" stroke="#36b5c9" stroke-width="2.2"><path d="M12,4 C4,4 4,20 12,26 L48,26 C56,20 56,4 48,4 C42,4 38,8 30,8 C22,8 18,4 12,4 Z"/><path d="M18,32 h24 M20,40 h20 M22,48 h16 M24,56 h12 M30,32 v40"/></svg>
    <h3>Dental Implant</h3>
    <p>Lorem ipsum dolor sit amet,<br>consectetur adipiscing elit, sed do<br>eiusmod tempor incididunt</p>
  </div>
  <div class="service" style="left:802px;top:236px">
    <svg width="74" height="80" viewBox="0 0 74 80"><rect x="16" y="4" width="46" height="8" rx="3" fill="none" stroke="#36b5c9" stroke-width="2.2"/><path d="M22,4 v-2 M30,4 v-2 M38,4 v-2 M46,4 v-2" stroke="#36b5c9" stroke-width="2"/><use href="#tooth" x="8" y="16" width="54" height="62"/></svg>
    <h3>Dental Hygiene</h3>
    <p>Lorem ipsum dolor sit amet,<br>consectetur adipiscing elit, sed do<br>eiusmod tempor incididunt</p>
  </div>

  <div class="service" style="left:88px;top:560px">
    <svg width="70" height="70" viewBox="0 0 70 70" fill="none" stroke="#36b5c9" stroke-width="2.2"><path d="M8,10 L20,8 L26,22 L18,28 C22,38 30,46 40,50 L46,42 L60,48 L58,60 C30,62 6,40 8,10 Z"/><circle cx="44" cy="22" r="14"/><path d="M44,14 v16 M36,22 h16"/></svg>
    <h3>Emergency Services</h3>
    <p>Lorem ipsum dolor sit amet,<br>consectetur adipiscing elit, sed do<br>eiusmod tempor incididunt</p>
  </div>
  <div class="service" style="left:447px;top:556px">
    <svg width="74" height="74" viewBox="0 0 74 74"><circle cx="37" cy="37" r="33" fill="none" stroke="#36b5c9" stroke-width="2.2"/><circle cx="37" cy="37" r="26" fill="none" stroke="#36b5c9" stroke-width="1.6" stroke-dasharray="4 4"/><use href="#tooth" x="17" y="15" width="40" height="44"/></svg>
    <h3>Restorations</h3>
    <p>Lorem ipsum dolor sit amet,<br>consectetur adipiscing elit, sed do<br>eiusmod tempor incididunt</p>
  </div>
  <div class="service" style="left:790px;top:562px">
    <svg width="78" height="74" viewBox="0 0 78 74"><use href="#tooth" x="18" y="4" width="58" height="66"/><path d="M6,6 L26,42 M2,10 L10,2" stroke="#36b5c9" stroke-width="2.2" fill="none"/><path d="M16,36 C8,48 10,62 20,68 L26,66 L24,48" stroke="#36b5c9" stroke-width="2.2" fill="none"/></svg>
    <h3>Dentures</h3>
    <p>Lorem ipsum dolor sit amet,<br>consectetur adipiscing elit, sed do<br>eiusmod tempor incididunt</p>
  </div>
</section>

<!-- Procedure -->
<h2 class="abs serif" style="left:0;width:1200px;text-align:center;top:2422px;font-size:40px">Our Proceedure</h2>
<svg class="abs" style="left:0;top:2520px" width="1200" height="120" viewBox="0 2520 1200 120">
  <path d="M306,2578 C380,2620 470,2620 528,2578" fill="none" stroke="#36b5c9" stroke-width="2" stroke-dasharray="8 7"/>
  <path d="M638,2560 C710,2515 800,2515 868,2560" fill="none" stroke="#36b5c9" stroke-width="2" stroke-dasharray="8 7"/>
  <g fill="none" stroke="#36b5c9" stroke-width="4"><circle cx="251" cy="2581" r="38"/><circle cx="582" cy="2581" r="38"/><circle cx="922" cy="2581" r="38"/></g>
  <g font-family="Libre Baskerville, serif" font-size="48" fill="#36b5c9" text-anchor="middle"><text x="251" y="2598">1</text><text x="582" y="2598">2</text><text x="922" y="2598">3</text></g>
</svg>
<div class="step" style="left:131px;top:2641px"><h4>LOREM IPSUM</h4><p>Book your visit online or by phone<br>and pick a time that suits<br>your day best.</p></div>
<div class="step" style="left:462px;top:2641px"><h4>LOREM IPSUM</h4><p>Meet our team for a gentle exam,<br>digital x-rays and a clear talk<br>about your options.</p></div>
<div class="step" style="left:810px;top:2641px"><h4>LOREM IPSUM</h4><p>Follow your personal care plan<br>and enjoy a healthy smile with<br>easy regular checkups.</p></div>

<!-- Reviews -->
<h2 class="abs serif" style="left:0;width:1240px;text-align:center;top:2872px;font-size:40px">Customer Reviews</h2>
<svg class="abs" style="left:559px;top:2966px" width="78" height="78" viewBox="0 0 78 78">
  <circle cx="39" cy="39" r="39" fill="#36b5c9"/>
  <path d="M22,28 h14 v12 c0,8 -4,12 -10,14 l-2,-4 c4,-2 6,-4 6,-8 h-8 z M42,28 h14 v12 c0,8 -4,12 -10,14 l-2,-4 c4,-2 6,-4 6,-8 h-8 z" fill="#fff"/>
</svg>
<p class="abs" style="left:0;width:1200px;text-align:center;top:3073px;font-family:'Montserrat',sans-serif;font-style:italic;font-size:20px;line-height:32px;color:#444">Lorem ipsum dolor sit amet, consectetuer adipiscing elit.<br>Aenean commodo ligula eget dolor aenean massa.</p>
<svg class="abs" style="left:170px;top:3092px" width="24" height="30" viewBox="0 0 24 30"><path d="M18,2 L6,15 L18,28" fill="none" stroke="#222" stroke-width="3"/></svg>
<svg class="abs" style="left:1022px;top:3092px" width="24" height="30" viewBox="0 0 24 30"><path d="M6,2 L18,15 L6,28" fill="none" stroke="#222" stroke-width="3"/></svg>
<div class="abs" role="img" aria-label="Portrait of the reviewer" style="left:556px;top:3164px;width:74px;height:74px;border-radius:50%;background:linear-gradient(135deg,#e8d2c2,#b98b6f)"></div>
<div class="abs" style="left:0;width:1194px;text-align:center;top:3272px;font-family:'Raleway',sans-serif;font-weight:700;font-size:18px">NORA WHITFIELD</div>
<div class="abs" style="left:0;width:1194px;text-align:center;top:3298px;font-family:'Montserrat',sans-serif;font-size:11px;color:var(--teal)">MANAGER</div>

<!-- Booking form -->
<section class="abs" style="left:0;top:3389px;width:1200px;height:533px;background:var(--panel)">
  <svg class="abs" style="left:0;top:0" width="560" height="533" viewBox="0 0 560 533">
    <defs><linearGradient id="docGrad" x1="0" y1="0" x2="1" y2="1"><stop offset="0" stop-color="#d9dfe4"/><stop offset="0.55" stop-color="#c7a088"/><stop offset="1" stop-color="#6d9ad0"/></linearGradient></defs>
    <path d="M0,0 L538,0 C540,300 330,520 0,533 Z" fill="#36b5c9"/>
    <path d="M0,0 L524,0 C524,294 320,512 0,524 Z" fill="url(#docGrad)" role="img" aria-label="Photo of a masked dentist treating a patient"/>
  </svg>
  <div class="field" style="left:602px;top:124px;width:253px;height:38px">FULL NAME</div>
  <div class="field" style="left:878px;top:124px;width:255px;height:38px">EMAIL ADDRESS</div>
  <div class="field" style="left:602px;top:188px;width:253px;height:38px">PHONE NUMBER</div>
  <div class="field" style="left:878px;top:188px;width:255px;height:38px">SELECT SERVICE</div>
  <div class="field" style="left:602px;top:245px;width:531px;height:40px">SELECT DATE</div>
  <div class="field" style="left:602px;top:295px;width:531px;height:64px;align-items:flex-start;padding-top:12px">ADDITIONAL MESSAGE</div>
  <div class="abs pill" style="left:602px;top:395px;width:231px;height:46px;line-height:46px;font-size:18px;font-weight:600">Get Appointment</div>
</section>

<!-- Footer -->
<footer class="abs" style="left:0;top:3922px;width:1200px;height:393px;background:var(--teal)">
  <div class="abs brand" style="left:77px;top:130px;color:var(--white);width:220px;text-align:center">Maplecrest Dentistry</div>
  <div class="abs" style="left:149px;top:206px;width:20px;height:20px;border-radius:50%;background:var(--white)"></div>
  <div class="abs" style="left:196px;top:206px;width:20px;height:20px;border-radius:50%;background:var(--white)"></div>

  <div class="abs foot-h" style="left:384px;top:82px">Quick Links</div>
  <div class="abs foot-link" style="left:397px;top:135px">Home</div>
  <div class="abs foot-link" style="left:397px;top:171px">Services</div>
  <div class="abs foot-link" style="left:397px;top:208px">Pricing</div>
  <div class="abs foot-link" style="left:397px;top:245px">About</div>
  <div class="abs foot-link" style="left:397px;top:282px">Contact</div>

  <div class="abs foot-h" style="left:593px;top:82px">Contact Nfo</div>
  <svg class="abs" style="left:592px;top:128px" width="20" height="20" viewBox="0 0 20 20"><path d="M3,2 L7,1 L9,6 L6,8 C7,11 9,13 12,14 L14,11 L19,13 L18,17 C9,18 2,11 3,2 Z" fill="#fff"/></svg>
  <div class="abs foot-txt" style="left:645px;top:128px">(555) 014 2230</div>
  <svg class="abs" style="left:592px;top:170px" width="22" height="18" viewBox="0 0 22 18"><path d="M1,6 L11,1 L21,6 L21,17 L1,17 Z" fill="#fff"/><path d="M1,6 L11,12 L21,6" fill="none" stroke="#36b5c9" stroke-width="1.5"/></svg>
  <div class="abs foot-txt" style="left:645px;top:169px">hello@maplecrest.example</div>
  <svg class="abs" style="left:594px;top:209px" width="18" height="24" viewBox="0 0 18 24"><path d="M9,23 C3,14 1,11 1,8 A8,8 0 0 1 17,8 C17,11 15,14 9,23 Z" fill="#fff"/><circle cx="9" cy="8" r="3" fill="#36b5c9"/></svg>
  <div class="abs foot-txt" style="left:645px;top:208px">Elmwood Plaza,<br>210 Harbor Lane,<br>Riverside 5021</div>
  <svg class="abs" style="left:592px;top:281px" width="20" height="20" viewBox="0 0 20 20"><circle cx="10" cy="10" r="9" fill="#fff"/><path d="M10,5 V10 L14,12" fill="none" stroke="#36b5c9" stroke-width="1.8" stroke-linecap="round"/></svg>
  <div class="abs foot-txt" style="left:645px;top:280px">Mon–Fri: 8:00 am – 6:00 pm<br>Sat: 9:00 am – 2:00 pm</div>

  <div class="abs foot-h" style="left:944px;top:82px">Stay Up-To-Date</div>
  <div class="abs" style="left:939px;top:154px;width:197px;height:34px;border-radius:17px;background:var(--teal-dark);color:var(--white);font-family:'Montserrat',sans-serif;font-weight:500;font-size:13px;text-align:center;line-height:34px">EMAIL ADDRESS</div>
  <div class="abs" style="left:939px;top:201px;width:197px;height:34px;border-radius:17px;background:var(--white);color:var(--teal);font-family:'Montserrat',sans-serif;font-weight:500;font-size:13px;text-align:center;line-height:34px">SUBSCRIBE NOW</div>

  <div class="abs" style="left:0;width:1164px;text-align:center;top:360px;font-family:'Montserrat',sans-serif;font-size:11px;color:var(--white)">© 2025 DENTAL WEBSITE. ALL RIGHTS RESERVED.</div>
</footer>

</body>
</html>
```